Website Design for a holiday home letting busines

We require a redesign of our present website www.fernbrookstays.com. We want the website to stand out and look professional and clean to make holiday hunters want to book a caravan or lodge holiday with us. Our logo is red however we DO NOT want the website to be red. We want a natural colour scheme.

The final design should communicate that we are a professional company to book with.

On the home page we require;
Overview of company
Photo
Search box for holiday (check in)
Late Deals
Reviews
News

We would like the following pages designed; home page, available dates page, caravans page, content page.

The website should be responsive for smart phones. One website I do like is http://www.brimoveld.be/nl/

Target Market(s)

Families

Industry/Entity Type

Travel

Number of Pages Required

5+ page

Font styles to use
Serif

Requirements
Must have
• The project must be responsive for mobile phones and tablets.
• Ability to search for holiday home holidays
• We want a natural colour scheme.
Nice to have
• A style we like is http://www.brimoveld.be/nl/
Should not have
• Do not use red as a colour for the website. Our logo is red so this is the only time we want this used.

```html
<!DOCTYPE html>
<html lang="en">
<head>
<meta charset="utf-8">
<title>Fernbrook Stays – Private Holiday Rentals</title>
<link href="https://fonts.googleapis.com/css2?family=Open+Sans:wght@400;600;700&family=Roboto+Slab:wght@400;700&display=swap" rel="stylesheet">
<style>
:root{
  --teal:#1e9b8f;
  --teal-dark:#167a70;
  --brand:#c8312f;
  --ink:#333;
  --muted:#888;
  --line:#e3e3e3;
  --pale:#f5f5f3;
  --footer:#2c2c2c;
  --footer-deep:#222;
  --white:#fff;
}
*{box-sizing:border-box;margin:0;padding:0}
html,body{width:1200px;height:2936px;overflow:hidden}
body{font-family:"Open Sans",Arial,sans-serif;color:var(--ink);font-size:13px;background:var(--white);position:relative}
h1,h2,h3,h4{font-family:"Roboto Slab",Georgia,serif}
.wrap{width:1000px;margin:0 auto;position:relative}

/* header */
.topbar{height:112px}
.topbar .wrap{display:flex;align-items:center;height:112px}
.brand{display:flex;align-items:center;gap:12px}
.brand-dot{width:46px;height:46px;border-radius:50%;background:var(--brand)}
.brand-name{font-family:"Roboto Slab",Georgia,serif;font-weight:700;font-size:30px;color:var(--brand)}
.brand-sub{font-size:11px;color:var(--muted);margin-top:2px}
.contact-strip{margin-left:auto;display:flex;align-items:center;gap:26px;font-size:13px;color:#555}
.contact-strip span{display:flex;align-items:center;gap:8px}
.ico{width:28px;height:28px;border-radius:50%;background:var(--teal);display:flex;align-items:center;justify-content:center}
.btn{display:inline-block;background:var(--teal);color:var(--white);font-weight:700;font-size:12px;text-transform:uppercase;padding:11px 22px;border-radius:2px}
.mainnav{height:38px;background:var(--teal)}
.mainnav ul{list-style:none;display:flex;justify-content:space-between;width:1000px;margin:0 auto;height:38px;align-items:center}
.mainnav li{color:var(--white);font-size:13px;font-weight:600;padding:0 10px;line-height:38px}
.mainnav li.active{background:var(--teal-dark)}

/* hero */
.hero{height:510px;position:relative;background:linear-gradient(100deg,#8a5a3c 0%,#b07a55 35%,#6e6a60 60%,#4b4f4a 100%)}
.hero-text{position:absolute;left:720px;top:175px;color:var(--white)}
.hero-text h1{font-size:38px;font-weight:700}
.hero-text p{font-size:14px;margin:10px 0 22px;width:320px;line-height:1.5}
.search{position:absolute;left:190px;top:455px;width:820px;height:42px;display:flex;background:var(--white);box-shadow:0 2px 8px rgba(0,0,0,.25)}
.search .field{flex:1;border-right:1px solid var(--line);padding:0 14px;display:flex;align-items:center;justify-content:space-between;font-size:12px;color:#666}
.search .go{background:var(--teal);color:var(--white);font-weight:700;font-size:13px;width:130px;display:flex;align-items:center;justify-content:center;text-transform:uppercase}

/* welcome */
.welcome{height:380px;padding-top:70px}
.welcome .wrap{display:flex;gap:40px}
.video{width:340px;height:170px;margin-top:40px;background:linear-gradient(135deg,#7f9a7a,#b8c2a4 60%,#8b7d65);position:relative}
.video svg{position:absolute;left:140px;top:55px}
.welcome-copy{flex:1}
.welcome-copy h2{font-size:28px;color:#333;margin-bottom:16px}
.welcome-copy p{line-height:1.75;color:#777;margin-bottom:24px}

/* section titles */
.sec-title{text-align:center;font-family:"Roboto Slab",Georgia,serif;font-weight:700;font-size:30px;text-transform:uppercase;color:#333}
.sec-title::after{content:"";display:block;width:60px;height:3px;background:var(--teal);margin:12px auto 0}

/* property cards */
.stock{height:490px;padding-top:36px;background:var(--pale)}
.cards{display:flex;gap:20px;margin-top:40px}
.card{width:235px;background:var(--white);border:1px solid var(--line)}
.card .photo{height:140px}
.card .body{padding:12px 12px 8px}
.meta{font-size:10px;color:var(--muted)}
.card h4{font-size:13px;text-transform:uppercase;margin:6px 0;color:#333}
.card p{font-size:11px;line-height:1.55;color:#888}
.card .foot{border-top:1px solid var(--line);margin-top:10px;padding:8px 12px;display:flex;justify-content:space-between;font-size:10px;color:var(--teal)}
.p1{background:linear-gradient(135deg,#b58a62,#e3d3bd)}
.p2{background:linear-gradient(135deg,#cfc6b4,#8d7b63)}
.p3{background:linear-gradient(135deg,#a27e59,#ddd6c7)}
.p4{background:linear-gradient(135deg,#d8d3b8,#8d6a4e)}

/* reviews */
.reviews{height:420px;padding-top:44px;background:linear-gradient(90deg,#4e4c48,#6f6c66 50%,#514f4b);color:var(--white);text-align:center}
.reviews .sec-title{color:var(--white)}
.quote{width:760px;margin:40px auto 0;font-size:14px;line-height:1.8;font-style:italic;position:relative}
.quote::before,.quote::after{font-family:"Roboto Slab",Georgia,serif;font-size:60px;position:absolute;opacity:.6}
.quote::before{content:"\201C";left:-50px;top:-20px}
.quote::after{content:"\201D";right:-50px;bottom:-50px}
.reviewer{display:flex;align-items:center;justify-content:center;gap:14px;margin-top:30px}
.avatar{width:60px;height:60px;border-radius:50%;background:#9c9a95;border:3px solid var(--white)}
.reviewer div{text-align:left;font-size:12px}
.reviewer b{display:block;font-size:13px}

/* late deals */
.deals{height:460px;padding-top:38px}
.deal .photo{height:150px;position:relative}
.badge{position:absolute;right:10px;bottom:-22px;width:48px;height:48px;border-radius:50%;background:var(--teal);color:var(--white);border:3px solid var(--white);font-size:11px;font-weight:700;display:flex;align-items:center;justify-content:center}
.deal .body{padding-top:18px}

/* news */
.news{height:350px;padding-top:24px}
.news .wrap{display:flex;gap:24px}
.col h3{font-size:22px;text-transform:uppercase;margin-bottom:16px;color:#333}
.col.list{width:330px}
.item{display:flex;gap:12px;margin-bottom:14px}
.item .thumb{width:100px;height:74px;flex:none}
.item b{display:block;font-size:11px;text-transform:uppercase}
.item small{font-size:10px;color:var(--teal)}
.item p{font-size:10px;color:#888;line-height:1.5;margin-top:3px}
.social-box{width:300px;height:300px;border:1px solid var(--line);box-shadow:0 1px 6px rgba(0,0,0,.12);padding:14px}
.social-head{display:flex;gap:10px;align-items:center;font-weight:700;color:#3b5372}
.social-head i{width:36px;height:36px;border-radius:50%;background:var(--brand)}
.social-head small{display:block;font-weight:400;font-size:10px;color:#888}
.faces{display:grid;grid-template-columns:repeat(6,1fr);gap:6px;margin-top:18px}
.faces i{height:36px;background:#c9c2b3}

/* footer */
.site-foot{height:140px;background:var(--footer);color:#bbb;padding-top:20px}
.site-foot .wrap{display:flex;gap:30px}
.site-foot h4{font-family:"Open Sans",Arial,sans-serif;font-size:13px;color:var(--white);text-transform:uppercase;margin-bottom:10px}
.fcol{width:220px;font-size:10px;line-height:1.6}
.fcol ul{list-style:none}
.fcol li::before{content:"› ";color:var(--teal)}
.fcol input{width:190px;height:22px;border:0;margin:6px 0;background:#fff}
.fcol .btn{padding:5px 12px;font-size:10px}
.soc li{display:flex;align-items:center;gap:8px;margin-bottom:3px}
.soc li::before{content:"";width:14px;height:14px;background:var(--teal)}
.copy-bar{height:36px;background:var(--footer-deep);color:#888;font-size:11px;line-height:36px}
.side-tab{position:absolute;right:0;top:2700px;width:26px;height:110px;background:var(--teal);color:var(--white);font-size:10px;font-weight:700;writing-mode:vertical-rl;text-align:center;line-height:26px}
</style>
</head>
<body>

<header class="topbar">
  <div class="wrap">
    <div class="brand">
      <div class="brand-dot"></div>
      <div>
        <div class="brand-name">Fernbrook Stays</div>
        <div class="brand-sub">At Mossgate Holiday Park</div>
      </div>
    </div>
    <div class="contact-strip">
      <span><i class="ico"><svg width="14" height="14" viewBox="0 0 24 24"><path fill="#fff" d="M6.6 10.8a15 15 0 0 0 6.6 6.6l2.2-2.2c.3-.3.7-.4 1-.2 1.1.4 2.3.6 3.6.6.6 0 1 .4 1 1V20c0 .6-.4 1-1 1A17 17 0 0 1 3 4c0-.6.4-1 1-1h3.5c.6 0 1 .4 1 1 0 1.3.2 2.5.6 3.6.1.3 0 .7-.2 1z"/></svg></i>01632 960 418</span>
      <span><i class="ico"><svg width="14" height="14" viewBox="0 0 24 24"><path fill="#fff" d="M3 5h18v14H3z M3 5l9 7 9-7" stroke="#1e9b8f" stroke-width="1.5"/></svg></i>hello@fernbrookstays.com</span>
      <span class="btn">Live Booking</span>
    </div>
  </div>
</header>

<nav class="mainnav">
  <ul>
    <li class="active">Home</li><li>News</li><li>Reviews</li><li>Caravans &amp; Lodges</li><li>Holidays</li><li>Planned Fleet</li><li>Mossgate Castle</li><li>Local Attractions</li><li>Contact Us</li>
  </ul>
</nav>

<section class="hero" role="img" aria-label="Couple relaxing together on a sofa inside a holiday lodge">
  <div class="hero-text">
    <h1>Private Holiday Rentals</h1>
    <p>Quality lodge &amp; caravan hire at Mossgate Castle Holiday Park. Book online today.</p>
    <span class="btn">View More</span>
  </div>
  <div class="search">
    <div class="field">Arriving <span>▾</span></div>
    <div class="field">Staying <span>▾</span></div>
    <div class="field">Adults <span>▾</span></div>
    <div class="field">Lodges &amp; Caravans <span>▾</span></div>
    <div class="go">Book Now</div>
  </div>
</section>

<section class="welcome">
  <div class="wrap">
    <div class="video" role="img" aria-label="Video still of a lodge set among trees">
      <svg width="60" height="60" viewBox="0 0 60 60"><circle cx="30" cy="30" r="28" fill="rgba(0,0,0,.45)" stroke="#fff" stroke-width="2"/><path d="M24 18l18 12-18 12z" fill="#fff"/></svg>
    </div>
    <div class="welcome-copy">
      <h2>Welcome to Fernbrook Stays</h2>
      <p>We have lovely lodges and caravans available to hire on a private basis at a well loved coastal holiday park. Every home is cleaned and checked before you arrive, with fresh linen, a fully fitted kitchen and plenty of space for the whole family to relax. Take a look at our homes, choose your dates and book securely online in a few simple steps. If you would like to talk to us about your stay, our friendly team is always happy to help.</p>
      <span class="btn">View More</span>
    </div>
  </div>
</section>

<section class="stock">
  <div class="wrap">
    <h2 class="sec-title">Our Caravans and Lodges</h2>
    <div class="cards">
      <article class="card"><div class="photo p1" role="img" aria-label="Caravan lounge interior"></div><div class="body"><div class="meta">Caravan type • Lodge</div><h4>New Harbury</h4><p>Lorem ipsum is simply dummy text of the printing and typesetting industry standard.</p></div><div class="foot"><span>Sleeps 6</span><span>2 Bed</span><span>View</span></div></article>
      <article class="card"><div class="photo p2" role="img" aria-label="Lodge kitchen and dining area"></div><div class="body"><div class="meta">Caravan type • Lodge</div><h4>The Wyndham</h4><p>Lorem ipsum is simply dummy text of the printing and typesetting industry standard.</p></div><div class="foot"><span>Sleeps 6</span><span>3 Bed</span><span>View</span></div></article>
      <article class="card"><div class="photo p3" role="img" aria-label="Caravan fitted kitchen"></div><div class="body"><div class="meta">Caravan type • Lodge</div><h4>The Alderton</h4><p>Lorem ipsum is simply dummy text of the printing and typesetting industry standard.</p></div><div class="foot"><span>Sleeps 4</span><span>2 Bed</span><span>View</span></div></article>
      <article class="card"><div class="photo p4" role="img" aria-label="Lodge living room with flowers"></div><div class="body"><div class="meta">Caravan type • Lodge</div><h4>New Harbury</h4><p>Lorem ipsum is simply dummy text of the printing and typesetting industry standard.</p></div><div class="foot"><span>Sleeps 8</span><span>3 Bed</span><span>View</span></div></article>
    </div>
  </div>
</section>

<section class="reviews" role="img" aria-label="Softly darkened lodge interior behind guest reviews">
  <h2 class="sec-title">Reviews</h2>
  <p class="quote">Lorem ipsum is simply dummy text of the printing and typesetting industry. Lorem ipsum has been the industry standard dummy text ever since the 1500s, when an unknown printer took a galley of type and scrambled it to make a type specimen book.</p>
  <div class="reviewer"><div class="avatar" role="img" aria-label="Guest portrait"></div><div><b>Hannah Reeve</b>Family holiday</div></div>
</section>

<section class="deals">
  <div class="wrap">
    <h2 class="sec-title">Late Deals</h2>
    <div class="cards">
      <article class="card deal"><div class="photo p1" role="img" aria-label="Caravan lounge"><span class="badge">£199</span></div><div class="body"><div class="meta">Caravan type • Lodge</div><h4>The Larchmere<br>Friday 19 Sep 2014 (3 nights)</h4></div><div class="foot"><span>Sleeps 6</span><span>2 Bed</span><span>Book</span></div></article>
      <article class="card deal"><div class="photo p2" role="img" aria-label="Lodge dining area"><span class="badge">£249</span></div><div class="body"><div class="meta">Caravan type • Lodge</div><h4>The Alderton<br>Friday 19 Sep 2014 (3 nights)</h4></div><div class="foot"><span>Sleeps 4</span><span>2 Bed</span><span>Book</span></div></article>
      <article class="card deal"><div class="photo p3" role="img" aria-label="Caravan bedroom"><span class="badge">£179</span></div><div class="body"><div class="meta">Caravan type • Lodge</div><h4>The Larchmere<br>Friday 19 Sep 2014 (3 nights)</h4></div><div class="foot"><span>Sleeps 6</span><span>3 Bed</span><span>Book</span></div></article>
      <article class="card deal"><div class="photo p4" role="img" aria-label="Lodge living room"><span class="badge">£229</span></div><div class="body"><div class="meta">Caravan type • Lodge</div><h4>The Larchmere<br>Friday 19 Sep 2014 (3 nights)</h4></div><div class="foot"><span>Sleeps 8</span><span>3 Bed</span><span>Book</span></div></article>
    </div>
  </div>
</section>

<section class="news">
  <div class="wrap">
    <div class="col list">
      <h3>Latest News</h3>
      <div class="item"><div class="thumb p2" role="img" aria-label="Lodge exterior"></div><div><b>Eco-friendly lodges</b><small>Sep 20, 2014</small><p>New energy saving lodges arrive on the park this autumn for families.</p></div></div>
      <div class="item"><div class="thumb p3" role="img" aria-label="Caravan interior"></div><div><b>Site refurbishment</b><small>Sep 22, 2014</small><p>Fresh paths, lighting and play areas are being added across the park.</p></div></div>
    </div>
    <div class="col list">
      <h3>Blog Feed</h3>
      <div class="item"><div class="thumb p4" role="img" aria-label="Caravans on a green field"></div><div><b>Weekend family breaks</b><small>Sep 20, 2014</small><p>Our top ideas for short stays with young children near the coast.</p></div></div>
      <div class="item"><div class="thumb p1" role="img" aria-label="Lodge decking"></div><div><b>Walks near the park</b><small>Sep 22, 2014</small><p>Gentle routes through woods and along the beach for every age.</p></div></div>
    </div>
    <div class="social-box">
      <div class="social-head"><i></i><div>Community Page<small>Fernbrook Stays · 1,240 likes</small></div></div>
      <div class="faces" role="img" aria-label="Grid of follower profile pictures">
        <i></i><i></i><i></i><i></i><i></i><i></i><i></i><i></i><i></i><i></i><i></i><i></i><i></i><i></i><i></i><i></i><i></i><i></i>
      </div>
    </div>
  </div>
</section>

<footer>
  <div class="site-foot">
    <div class="wrap">
      <div class="fcol"><h4>Quick Links</h4><ul><li>Home</li><li>News</li><li>Reviews</li><li>Caravans &amp; Lodges</li><li>Holidays</li><li>Contact Us</li></ul></div>
      <div class="fcol"><h4>Contact Details</h4>Fernbrook Stays Ltd<br>Unit 4, Mossgate Holiday Park<br>Coast Road, Northfield NF1 2AB<br>01632 960 418<br>hello@fernbrookstays.com</div>
      <div class="fcol"><h4>Newsletter Signup</h4>Join our list for late deals and park news.<br><input aria-label="Email address"><br><span class="btn">Subscribe</span></div>
      <div class="fcol"><h4>Social Media Links</h4><ul class="soc"><li>Community Page</li><li>Updates</li><li>Network</li><li>Circles</li></ul></div>
    </div>
  </div>
  <div class="copy-bar"><div class="wrap">Copyright 2014 fernbrookstays.com. All rights reserved.</div></div>
</footer>

<div class="side-tab">Enquire</div>
</body>
</html>
```